DUXOVE Flyer

We would like the option of being able to fill in a text box so we would need an editable file to type in our information.
You can add wording to it yourself where you see fit
We would like better designs than the ones we are sending as well.
We would like the lumo grove logo add on the flyer. We want the exact logo but not the back ground. We would like the logo to show up multiple times if possible.
You are free to be creative with the design. If you have ideas that are not listed in the description, feel free to design them.
Thanks!!!
Family Insurance

```html
<!DOCTYPE html>
<html lang="en">
<head>
<meta charset="utf-8">
<title>DUXOVE Flyer – lumo grove Family Insurance</title>
<link rel="stylesheet" href="https://fonts.googleapis.com/css2?family=Zilla+Slab:wght@500;600;700&family=Open+Sans:wght@400;600&family=Roboto:wght@400&display=swap">
<style>
  :root {
    --stage: #d0d0d0;
    --cream: #e6e2d6;
    --charcoal: #383838;
    --charcoal-deep: #333333;
    --brand-red: #d71f26;
    --ink: #2b2b2b;
    --body-text: #5a5650;
    --rule: #a29d92;
    --stone: #6f6a66;
    --white: #ffffff;
  }
  * { box-sizing: border-box; margin: 0; padding: 0; }
  html, body { width: 1200px; height: 800px; overflow: hidden; }
  body { background: var(--stage); position: relative; font-family: "Open Sans", sans-serif; }

  .flyer {
    position: absolute; left: 338px; top: 20px;
    width: 525px; height: 760px;
    background: var(--cream);
    box-shadow: 0 14px 30px rgba(0,0,0,.25);
    overflow: hidden;
  }

  /* Header */
  .flyer-header { position: absolute; left: 0; top: 0; width: 100%; height: 105px; }
  .brand-panel {
    position: absolute; left: 0; top: 0; width: 235px; height: 105px;
    background: var(--cream);
    display: flex; align-items: center; gap: 8px; padding-left: 20px;
  }
  .brand-dot { width: 26px; height: 26px; border-radius: 50%; background: var(--brand-red); }
  .brand-name {
    font-family: "Zilla Slab", serif; font-weight: 700; font-size: 30px;
    color: var(--brand-red); letter-spacing: -0.5px;
  }
  .contact-panel {
    position: absolute; left: 235px; top: 0; right: 0; height: 105px;
    background: var(--charcoal);
    padding: 40px 24px 0 0; text-align: right; font-style: normal;
    font-family: "Roboto", sans-serif; font-size: 11.5px; line-height: 1.2; color: var(--white);
  }

  /* Hero */
  .hero { position: absolute; left: 0; top: 105px; width: 100%; height: 250px; }
  .hero-photo {
    position: absolute; inset: 0;
    background: linear-gradient(180deg, #6f7276 0%, #9a9ea2 45%, #8d8579 72%, #76695a 100%);
  }
  .hero-copy { position: absolute; left: 22px; top: 50px; display: flex; flex-direction: column; align-items: flex-start; gap: 5px; }
  .hero-line {
    background: var(--charcoal); color: var(--white);
    font-family: "Zilla Slab", serif; font-weight: 500; font-size: 21px;
    text-transform: uppercase; line-height: 1; padding: 3px 10px 2px 14px;
  }
  .hero-points {
    list-style: none; margin-top: 2px; background: var(--charcoal);
    padding: 5px 14px 6px 12px; width: 200px;
    font-size: 7px; line-height: 1.55; color: var(--white);
  }
  .hero-points li { position: relative; padding-left: 12px; }
  .hero-points li::before {
    content: ""; position: absolute; left: 0; top: 3px;
    width: 5px; height: 5px; border-radius: 50%; background: var(--white);
  }

  /* Services */
  .services { position: absolute; left: 0; top: 355px; width: 100%; height: 250px; background: var(--cream); }
  .column { position: absolute; top: 22px; }
  .column-left { left: 22px; width: 205px; }
  .column-right { left: 270px; width: 225px; }
  .divider { position: absolute; left: 250px; top: 28px; width: 1px; height: 200px; background: var(--rule); }
  .section-kicker {
    font-family: "Zilla Slab", serif; font-weight: 700; font-size: 16px;
    color: var(--brand-red); text-transform: uppercase; line-height: 1;
  }
  .section-title {
    font-family: "Zilla Slab", serif; font-weight: 600; font-size: 18px;
    color: var(--ink); text-transform: uppercase; line-height: 1.1; margin-bottom: 8px;
  }
  .body-copy { font-size: 7px; line-height: 1.55; color: var(--body-text); margin-bottom: 22px; }

  .call-badge { position: absolute; left: 270px; top: 120px; width: 175px; height: 100px; }
  .call-badge svg { position: absolute; inset: 0; }
  .call-text { position: absolute; left: 0; top: 28px; width: 175px; text-align: center; color: var(--white); }
  .call-heading { font-family: "Zilla Slab", serif; font-weight: 500; font-size: 19px; text-transform: uppercase; line-height: 1; }
  .call-number { font-family: "Roboto", sans-serif; font-size: 13px; margin-top: 5px; letter-spacing: .5px; }

  /* Footer */
  .team-band { position: absolute; left: 0; top: 605px; width: 100%; height: 115px; background: var(--charcoal-deep); }
  .team-photos { position: absolute; left: 137px; top: 8px; width: 250px; height: 96px; }
  .team-photo {
    position: absolute; top: 0; width: 92px; height: 92px; border-radius: 50%;
    border: 2px solid var(--brand-red);
  }
  .team-photo.desk { left: 0; background: linear-gradient(135deg, #cfd3d8, #8e9299); }
  .team-photo.advisor { left: 72px; background: linear-gradient(135deg, #8aa0ac, #5d6b76); z-index: 2; }
  .team-photo.meeting { left: 144px; background: linear-gradient(135deg, #d9cbb8, #6e6257); }
  .accent-band {
    position: absolute; left: 0; top: 720px; width: 100%; height: 40px; background: var(--brand-red);
    display: flex; align-items: center; justify-content: center; gap: 6px;
  }
  .accent-band .brand-dot { width: 14px; height: 14px; background: var(--white); }
  .accent-band .brand-name { font-size: 18px; color: var(--white); }
</style>
</head>
<body>
  <article class="flyer">
    <header class="flyer-header">
      <div class="brand-panel">
        <span class="brand-dot"></span>
        <span class="brand-name">lumo grove</span>
      </div>
      <address class="contact-panel">
        88 harbor lane millbrook 20417<br>
        hello@lumogrove.com<br>
        lumogrove.com
      </address>
    </header>

    <section class="hero">
      <div class="hero-photo" role="img" aria-label="Businessman holding an umbrella against wind and flying rocks on a hillside under a stormy sky"></div>
      <div class="hero-copy">
        <h1 class="hero-line">We Are</h1>
        <div class="hero-line">Family Insurance</div>
        <div class="hero-line">Built to Protect</div>
        <ul class="hero-points">
          <li>Family cover built around your home</li>
          <li>Clear plans with no hidden fees</li>
          <li>Local agents ready every day</li>
        </ul>
      </div>
    </section>

    <section class="services">
      <div class="column column-left">
        <p class="section-kicker">Best</p>
        <h2 class="section-title">Management</h2>
        <p class="body-copy">We plan every policy with care, review it each year and keep your family cover simple to understand.</p>
        <p class="body-copy">Our team tracks claims from first call to final payment so you never wait long for an answer.</p>
        <p class="body-copy">Home, car and life plans sit together in one place, making renewals quick and costs easy to follow.</p>
      </div>
      <div class="divider"></div>
      <div class="column column-right">
        <p class="section-kicker">Happy</p>
        <h2 class="section-title">Customers</h2>
        <p class="body-copy">Thousands of local families trust us to protect what matters most, and most renew with us year after year.</p>
      </div>
      <div class="call-badge">
        <svg viewBox="0 0 175 100" width="175" height="100" aria-hidden="true">
          <circle cx="50" cy="50" r="48" fill="#d71f26"/>
          <circle cx="125" cy="50" r="48" fill="#6f6a66" fill-opacity=".88"/>
        </svg>
        <div class="call-text">
          <p class="call-heading">For Free Call</p>
          <p class="call-number">055-310-2468-00</p>
        </div>
      </div>
    </section>

    <section class="team-band">
      <div class="team-photos">
        <div class="team-photo desk" role="img" aria-label="Hands working on a laptop at an office desk"></div>
        <div class="team-photo advisor" role="img" aria-label="Smiling advisor in a grey suit"></div>
        <div class="team-photo meeting" role="img" aria-label="Colleagues reviewing papers at a meeting table"></div>
      </div>
    </section>
    <footer class="accent-band">
      <span class="brand-dot"></span>
      <span class="brand-name">lumo grove</span>
    </footer>
  </article>
</body>
</html>
```